Rack card for marketing

Office to office marketing for knee pain treatment

Target Market(s)

Medical Offices, Retired patients looking to maintain active lifestlye. Family practice medical offices

Industry/Entity Type

Medical

Colors
0054AA
0677BA
7BADD7
CADEEF
E8F1F8

Requirements
Must have
• Font that matches logo, GRM logo, graphic of a retiree who looks active and happy versus a knee graphic
Nice to have
• The best ever rack card!!! Easy to Read, simplicity is key.

```html
<!DOCTYPE html>
<html lang="en">
<head>
<meta charset="utf-8">
<title>GRM Knee Pain Rack Card</title>
<link href="https://fonts.googleapis.com/css2?family=Roboto+Condensed:ital,wght@0,400;0,700;1,700&family=Russo+One&display=swap" rel="stylesheet">
<style>
  :root {
    --brand-blue: #235f85;
    --brand-deep: #1e5780;
    --ink-blue: #245d86;
    --soft-gray: #cfd1d4;
    --light-panel: #dde6ee;
    --dark-text: #454545;
    --white: #ffffff;
    --page: #ffffff;
  }
  * { margin: 0; padding: 0; box-sizing: border-box; }
  html, body { width: 1121px; height: 1200px; overflow: hidden; background: var(--page); }
  body { position: relative; font-family: "Roboto Condensed", Arial, sans-serif; }

  .rack-card {
    position: absolute; left: 315px; top: 80px;
    width: 576px; height: 1223px;
    transform: scale(0.85); transform-origin: top left;
    background: var(--white); overflow: hidden;
  }
  .card-shapes { position: absolute; inset: 0; }

  .tagline {
    position: absolute; right: 324px; top: 44px; text-align: right;
    color: var(--ink-blue); font-size: 27px; line-height: 28.5px; letter-spacing: 0.5px;
  }
  .header-divider { position: absolute; left: 283px; top: 30px; width: 3px; height: 142px; background: var(--ink-blue); }
  .brand-mark { position: absolute; left: 322px; top: 52px; color: var(--ink-blue); font-weight: 400; }
  .brand-mark .brand-name { font-size: 58px; line-height: 60px; letter-spacing: 1px; }
  .brand-mark .brand-sub { font-size: 22px; line-height: 24px; }

  .treatment-list {
    position: absolute; left: 20px; top: 254px; list-style: none;
    color: var(--ink-blue); font-style: italic; font-weight: 700; font-size: 25px; line-height: 30.6px; letter-spacing: 0.6px;
  }
  .treatment-list li { padding-left: 23px; position: relative; }
  .treatment-list li::before { content: "•"; position: absolute; left: 0; font-style: normal; }
  .treatment-list .cont { padding-left: 48px; }
  .treatment-list .cont::before { content: none; }

  .procedures { position: absolute; left: 0; right: 0; top: 730px; text-align: center; color: var(--white); }
  .procedures-label {
    display: inline-block; background: var(--light-panel); color: var(--brand-deep);
    font-weight: 700; font-size: 23px; line-height: 27px; padding: 0 6px; margin-bottom: 9px;
  }
  .procedures-list { list-style: none; font-weight: 700; font-size: 24.5px; line-height: 31.6px; letter-spacing: 0.6px; }

  .appointment { position: absolute; left: 0; right: 0; top: 997px; text-align: center; }
  .appointment-title { font-family: "Russo One", sans-serif; color: var(--ink-blue); font-size: 28px; line-height: 30px; letter-spacing: 0.5px; }
  .physician { color: var(--dark-text); font-weight: 700; font-size: 33px; line-height: 36px; margin-top: 6px; }
  .specialty { color: var(--dark-text); font-weight: 700; font-size: 23px; line-height: 30px; letter-spacing: 0.5px; }

  .contact-footer {
    position: absolute; left: 0; right: 0; top: 1155px; text-align: center;
    color: var(--white); font-size: 22px; line-height: 29px; letter-spacing: 0.6px;
  }
  .contact-footer .gap { display: inline-block; width: 18px; }
</style>
</head>
<body>
<div class="rack-card">
  <svg class="card-shapes" width="576" height="1223" viewBox="0 0 576 1223">
    <defs>
      <linearGradient id="headerFade" x1="0" y1="0" x2="0" y2="1">
        <stop offset="0" stop-color="#ffffff"/><stop offset="1" stop-color="#ececee"/>
      </linearGradient>
      <linearGradient id="kneePhoto" x1="0" y1="0" x2="1" y2="1">
        <stop offset="0" stop-color="#5e6266"/>
        <stop offset="0.45" stop-color="#c9b3a6"/>
        <stop offset="0.65" stop-color="#e0826f"/>
        <stop offset="1" stop-color="#e7e8ea"/>
      </linearGradient>
      <linearGradient id="parkPhoto" x1="0" y1="0" x2="0" y2="1">
        <stop offset="0" stop-color="#5f8a3a"/>
        <stop offset="0.55" stop-color="#c9cfc0"/>
        <stop offset="1" stop-color="#7f9a5a"/>
      </linearGradient>
    </defs>
    <rect x="0" y="0" width="576" height="230" fill="url(#headerFade)"/>
    <rect x="268" y="195" width="308" height="520" fill="url(#kneePhoto)" role="img" aria-label="Photo of a person holding a painful knee, highlighted in red"/>
    <path d="M0 220 Q260 170 576 212 L576 250 Q260 180 0 250 Z" fill="var(--brand-blue)"/>
    <path d="M0 675 Q120 710 300 712 L576 712 L576 1223 L0 1223 Z" fill="var(--soft-gray)"/>
    <path d="M0 698 Q150 720 330 708 Q470 700 576 680 L576 995 L0 995 Z" fill="var(--brand-blue)"/>
    <path d="M0 1025 Q290 950 576 1025 L576 1141 L0 1141 Z" fill="var(--soft-gray)"/>
    <path d="M0 1050 Q290 965 576 1050 L576 1141 L0 1141 Z" fill="var(--white)"/>
    <rect x="0" y="1147" width="576" height="76" fill="var(--brand-blue)"/>
    <circle cx="443" cy="615" r="122" fill="#e9ecef"/>
    <circle cx="443" cy="615" r="116" fill="url(#parkPhoto)" role="img" aria-label="Photo of a happy active retiree riding a bicycle in a park"/>
  </svg>

  <div class="tagline">Comprehensive<br>Non-operative<br>Treatment<br>for Knee Pain</div>
  <div class="header-divider"></div>
  <div class="brand-mark">
    <div class="brand-name">GRM</div>
    <div class="brand-sub">Grove Regional Medicine</div>
  </div>

  <ul class="treatment-list">
    <li>Nonsurgical Options</li>
    <li>Customized Bracing</li>
    <li>Topical Medications</li>
    <li>Topical Supplements</li>
    <li>Evidence Based</li>
    <li class="cont">Supplementation</li>
    <li>Cryotherapy /</li>
    <li class="cont">Cold Compression</li>
    <li>Acupuncture /</li>
    <li class="cont">Electrical Therapy</li>
    <li>Exercise Protocols</li>
    <li class="cont">Athletic Trainer</li>
    <li class="cont">Exercise Physiologist</li>
  </ul>

  <section class="procedures">
    <div class="procedures-label">Procedures Offered</div>
    <ul class="procedures-list">
      <li>Interarticular Knee Injection</li>
      <li>Pes Anserine Bursa</li>
      <li>Genicular Nerve Block</li>
      <li>Genicular Radiofrequency Ablation</li>
      <li>HA (hyaluronic acid) Injections</li>
      <li>Relivex Injections</li>
    </ul>
  </section>

  <section class="appointment">
    <h2 class="appointment-title">SCHEDULE YOUR<br>APPOINTMENT TODAY</h2>
    <div class="physician">Martin Ellery, M.D.</div>
    <div class="specialty">Interventional Pain Management</div>
  </section>

  <footer class="contact-footer">
    <div>1820 Lakeview Ridge Dr., Orangewood, FL 34700</div>
    <div>Phone 352-555-0142<span class="gap"></span>Fax 352-555-0178</div>
  </footer>
</div>
</body>
</html>
```